【サイトマップ】
①TOP
②初めての方へ
③医師の紹介
④訪問診療について
⑤グループワーク
⑥漢方治療
⑦うつ病・双極性障害
⑧統合失調症
⑨認知症
⑩不安障害
⑪PMS・PMDD
⑫睡眠障害
⑬心身症
⑭発達障害
⑮お知らせ (一覧)
⑯お知らせ (詳細)
⑰ブログ (一覧)
⑱ブログ (詳細)
⑲お問い合せ・FAQ
⑳採用情報

【押していきたいメニュー】
⑥漢方治療
⑪PMS・PMDD

【デザインカラー】
ピンクなど淡い色合いにしていただければと存じます。

【デザインテイスト】
①清潔感
②優しい
③ナチュラル
※派手さやゴージャスなど敷居が高くなるイメージはNG×

【フォント】
游ゴシックか游明朝を使用してください。

【参考サイト(イメージに近いサイト)】
https://kaede-heart.example/

■参考にしたい部分
・優しさを感じるデザイン
・ユーザー目線を考えた構成(情報の分かりやすさ)

【ワイヤーフレーム】
http://hoshiweb.example.jp/client-check/tsubakiyume/wireframe/01
※構成は変えていただいて問題ございません。
またサイトマップと異なる情報が入っている箇所がございます。
サイトマップが最新情報となりますので、サイトマップの方に合わせてください。

【ロゴ】
http://hoshiweb.example.jp/client-check/tsubakiyume/rogo/10.A

【院の素材】
開業前なので、素材がございません。
清潔感があり、落ち着いている雰囲気を出し、
診療場所は完全個室の予定です。

【ブログ】
下記が開業に向け、書いているブログです。
もしデザイン作成に役立つ箇所がございましたら、
参考にしていただければ幸いです。
http://tsubaki487.example/

ピクセラ[ https://jp.pixela-stock.example/ ]で定期契約をしています。
クレジット購入のみのもの以外をご利用下さい。
また定期契約のものは弊社の負担となり、ランサー様に負担はありません。
カンプ画像を入れてください。
お世話になっております。
数多くのデザイン案を見てみたいので、
延長いたします。
皆様どうぞよろしくお願いいたします。

要望を的確に読み取って頂き、
一番近いデザインにしていただきました。

この度は当院のwebサイトTOPページを作成いただきまして誠にありがとうございます。
イメージしていたデザインよりもいいものができました。

また機会がございましたらぜひよろしくお願いいたします。

```html
<!DOCTYPE html>
<html lang="ja">
<head>
<meta charset="utf-8">
<title>つばきゆめクリニック</title>
<link href="https://fonts.googleapis.com/css2?family=Noto+Sans+JP:wght@400;500;700&family=Zen+Maru+Gothic:wght@500;700&display=swap" rel="stylesheet">
<style>
:root{
  --pink:#f19aa8;
  --pink-deep:#e9788c;
  --pink-soft:#fbe3e7;
  --pink-pale:#fdf1f3;
  --beige:#f9efe6;
  --green:#9fcf6a;
  --green-pale:#e9f4dc;
  --blue-pale:#e4f1f8;
  --text:#555;
  --muted:#888;
  --white:#fff;
}
*{margin:0;padding:0;box-sizing:border-box}
html,body{width:1200px;height:4844px;overflow:hidden}
body{font-family:"Noto Sans JP",sans-serif;color:var(--text);background:var(--white);font-size:15px;line-height:1.7}
.heading{font-family:"Zen Maru Gothic",sans-serif;font-weight:700;text-align:center;font-size:28px;color:#5a5a5a;letter-spacing:.08em}
.btn{display:block;margin:0 auto;width:260px;height:44px;border-radius:22px;background:var(--pink);color:var(--white);font-size:14px;text-align:center;line-height:44px;letter-spacing:.1em}
.blossom{position:absolute;border-radius:50%;background:radial-gradient(circle,#fbd0d8,#fde9ec 60%,rgba(255,255,255,0) 72%)}

/* header / hero */
.hero{position:relative;height:760px;overflow:hidden}
.hero-photo{position:absolute;left:260px;top:0;width:940px;height:760px;background:radial-gradient(circle at 75% 30%,#f4a9b9 0,#f7c9d3 18%,#fbe4ea 38%,#eef3f7 70%,#f6f7f9 100%)}
.hero-wave{position:absolute;left:0;top:0}
.site-header{position:absolute;left:0;top:0;width:1200px;height:120px}
.logo{position:absolute;left:60px;top:34px;display:flex;align-items:center;gap:12px}
.logo-mark{width:40px;height:40px;border-radius:50%;background:var(--pink)}
.logo-name{font-size:22px;font-weight:500;color:var(--pink-deep);letter-spacing:.06em}
.header-info{position:absolute;left:670px;top:30px;width:250px}
.header-info .lead{font-size:12px;color:var(--text);white-space:nowrap}
.tel{font-size:28px;font-weight:700;color:#555;letter-spacing:.02em;line-height:1.2;white-space:nowrap}
.header-hours{position:absolute;left:950px;top:30px;display:flex;flex-direction:column;gap:8px}
.hours-row{display:flex;gap:6px;font-size:12px;white-space:nowrap}
.hours-row span{padding:0 8px;background:var(--green);color:var(--white);border-radius:3px}
.contact-btn{width:200px;height:40px;line-height:40px;text-align:center;background:var(--green);color:var(--white);border-radius:4px;font-size:14px;flex-shrink:0}
.global-nav{position:absolute;left:110px;top:142px;display:flex;gap:50px;font-size:13px;color:#666}

/* news */
.news{position:relative;height:420px;padding-top:110px}
.news-inner{display:flex;width:760px;margin:0 auto;gap:60px}
.news-title{display:flex;align-items:center;gap:12px;font-family:"Zen Maru Gothic",sans-serif;font-size:26px;font-weight:700}
.news-title i{width:50px;height:50px;border-radius:50%;background:var(--pink-soft)}
.news-list{list-style:none;flex:1;font-size:13px}
.news-list li{display:flex;gap:16px;align-items:center;height:40px;border-bottom:1px dotted #e5c8cd}
.news-list .tag{background:var(--pink);color:var(--white);font-size:11px;padding:0 10px;border-radius:3px}
.news .btn{margin-top:50px}

/* worries */
.worries{position:relative;height:420px;padding-top:40px}
.worry-grid{display:grid;grid-template-columns:repeat(3,200px);gap:16px 28px;width:656px;margin:50px auto 0}
.worry-grid div{height:44px;background:var(--pink-soft);border-radius:4px;text-align:center;line-height:44px;font-size:14px}

/* features */
.features{position:relative;height:420px;padding-top:40px}
.features .band{position:absolute;left:0;top:240px;width:1200px;height:160px;background:var(--green-pale)}
.feature-list{position:relative;display:flex;gap:40px;width:960px;margin:50px auto 0}
.feature{width:293px}
.feature .photo{height:180px;background:linear-gradient(135deg,#eef3f8,#f8dde2)}
.feature h3{margin-top:10px;font-size:15px;color:var(--pink-deep);font-weight:500}
.feature p{font-size:12px;color:var(--muted)}

/* symptoms */
.symptoms{position:relative;height:700px;background:var(--beige);padding-top:60px}
.symptom-grid{display:grid;grid-template-columns:repeat(5,160px);gap:60px 40px;width:960px;margin:60px auto 0;justify-items:center}
.symptom-grid div{width:160px;height:160px;border-radius:50%;background:radial-gradient(circle,#fde7ec,#f7bcc8);display:flex;align-items:center;justify-content:center;font-size:15px;color:#6a5b5d}
.symptoms .btn{margin-top:60px;position:relative}

/* guide cards */
.guide{height:530px;padding-top:100px;display:flex;justify-content:center;gap:40px}
.guide-card{width:293px;height:240px;background:linear-gradient(135deg,#f6e6ea,#fbf5f6);border:1px solid #f1d4da;display:flex;align-items:center;justify-content:center}
.guide-card span{background:rgba(255,255,255,.85);padding:6px 20px;color:var(--pink-deep);font-size:20px;font-family:"Zen Maru Gothic",sans-serif;font-weight:700}

/* blog */
.blog{height:500px;padding-top:60px}
.blog-list{display:flex;gap:40px;width:960px;margin:50px auto 0}
.post{width:293px}
.post .photo{height:180px;background:linear-gradient(160deg,#cfe5f6,#f6cfd8)}
.post time{display:block;margin-top:8px;font-size:12px;color:var(--muted)}
.post h3{font-size:14px;font-weight:500}
.blog .btn{margin-top:40px}

/* banners */
.banners{position:relative;height:260px;padding-top:20px;background:linear-gradient(var(--white) 50%,var(--blue-pale) 50%)}
.banner-row{display:flex;gap:40px;width:960px;margin:0 auto}
.banner{width:460px;height:220px;background:linear-gradient(135deg,#fde8ec,#fff);border:1px solid #f1d4da;padding:40px 30px}
.banner strong{font-family:"Zen Maru Gothic",sans-serif;font-size:28px;color:var(--pink-deep);display:block}
.banner.recruit{background:linear-gradient(135deg,#fff,#fbe3e7)}

/* map */
.map{height:280px;background:linear-gradient(135deg,#e8ede8,#dfe7ee)}

/* footer */
.site-footer{position:relative;height:404px;background:var(--beige);padding-top:40px}
.footer-top{display:flex;justify-content:center;gap:30px;align-items:center}
.footer-body{display:flex;gap:60px;width:960px;margin:40px auto 0;font-size:12px}
.footer-address .box{margin-top:10px;width:300px;height:120px;background:var(--white);border:1px solid #e7d7cc}
.footer-nav{display:grid;grid-template-columns:repeat(3,160px);gap:4px 20px;list-style:none}
.footer-nav li::before{content:"›";color:var(--pink);margin-right:6px}
.copyright{position:absolute;bottom:0;left:0;width:1200px;height:44px;line-height:44px;text-align:center;background:var(--pink);color:var(--white);font-size:12px}
</style>
</head>
<body>

<section class="hero">
  <div class="hero-photo" role="img" aria-label="青空を背景に咲く桜の花の写真"></div>
  <svg class="hero-wave" width="1200" height="760" viewBox="0 0 1200 760">
    <path d="M0 0H620C520 180 380 320 420 520C450 660 560 720 620 760H0Z" fill="#fff"/>
    <path d="M0 700C300 640 700 760 1200 700V760H0Z" fill="#fff"/>
  </svg>
  <header class="site-header">
    <div class="logo"><span class="logo-mark"></span><span class="logo-name">つばきゆめクリニック</span></div>
    <div class="header-info">
      <p class="lead">お気軽にお問い合わせください</p>
      <p class="tel">☎ 00-0000-0000</p>
    </div>
    <div class="header-hours">
      <div class="hours-row"><span>診療</span>月・火・水・木・金・土</div>
      <div class="contact-btn">お問い合わせ</div>
    </div>
  </header>
  <nav class="global-nav"><span>TOP</span><span>当院について</span><span>診療のご案内</span><span>医師の紹介</span><span>診療の流れ</span><span>よくある質問</span></nav>
</section>

<section class="news">
  <div class="news-inner">
    <h2 class="news-title"><i></i>お知らせ</h2>
    <ul class="news-list">
      <li><time>2018.00.00</time><span class="tag">お知らせ</span>ホームページをリニューアルしました。</li>
      <li><time>2018.00.00</time><span class="tag">お知らせ</span>ホームページをリニューアルしました。</li>
    </ul>
  </div>
  <a class="btn">一覧を見る</a>
</section>

<section class="worries">
  <div class="blossom" style="left:0;top:180px;width:260px;height:200px"></div>
  <div class="blossom" style="left:960px;top:100px;width:200px;height:160px"></div>
  <h2 class="heading">このようなお悩みはありませんか？</h2>
  <div class="worry-grid">
    <div>気分が落ち込む</div><div>眠れない</div><div>不安感が強い</div>
    <div>集中力が続かない</div><div>疲れやすい</div><div>月経前のイライラが続く</div>
    <div>動悸・息苦しさ</div><div>食欲不振</div><div>対人関係がうまくいかない</div>
  </div>
</section>

<section class="features">
  <div class="band"></div>
  <h2 class="heading">当院の特徴</h2>
  <div class="feature-list">
    <div class="feature"><div class="photo" role="img" aria-label="ハートを持つ医師の手の写真"></div><h3>患者様に寄り添う治療</h3><p>お一人おひとりの気持ちに寄り添い、安心して相談できる診療を行います。</p></div>
    <div class="feature"><div class="photo" role="img" aria-label="女性医師が診察する様子の写真"></div><h3>女性医師による診療</h3><p>女性特有のお悩みも気軽にご相談いただける環境を整えています。</p></div>
    <div class="feature"><div class="photo" role="img" aria-label="問診票を記入する医師の写真"></div><h3>丁寧な問診</h3><p>じっくりお話を伺い、最適な治療方針をご提案いたします。</p></div>
  </div>
</section>

<section class="symptoms">
  <div class="blossom" style="left:20px;top:560px;width:220px;height:160px"></div>
  <div class="blossom" style="left:940px;top:560px;width:240px;height:160px"></div>
  <h2 class="heading">症状一覧</h2>
  <div class="symptom-grid">
    <div>うつ病</div><div>統合失調症</div><div>認知症</div><div>パニック障害</div><div>自律神経失調症</div>
    <div>睡眠障害</div><div>月経前症候群</div><div>心身症</div><div>発達障害</div>
  </div>
  <a class="btn">診療案内へ</a>
</section>

<section class="guide">
  <div class="guide-card" role="img" aria-label="受付スタッフの写真"><span>当院について</span></div>
  <div class="guide-card" role="img" aria-label="ハートを持つ女性の写真"><span>初めての方へ</span></div>
  <div class="guide-card" role="img" aria-label="医師の写真"><span>医師のご紹介</span></div>
</section>

<section class="blog">
  <h2 class="heading">ブログ</h2>
  <div class="blog-list">
    <article class="post"><div class="photo" role="img" aria-label="青空の写真"></div><time>2018.00.00</time><h3>ささやかな日常</h3></article>
    <article class="post"><div class="photo" role="img" aria-label="桜並木の写真"></div><time>2018.00.00</time><h3>開業準備を進めています</h3></article>
    <article class="post"><div class="photo" role="img" aria-label="桜と空の写真"></div><time>2018.00.00</time><h3>春の訪れ</h3></article>
  </div>
  <a class="btn">ブログ一覧へ</a>
</section>

<section class="banners">
  <div class="banner-row">
    <div class="banner" role="img" aria-label="明るい待合室の写真"><strong>お気軽にお問い合わせください</strong>☎ 00-0000-0000</div>
    <div class="banner recruit" role="img" aria-label="笑顔のスタッフの写真"><strong>スタッフ募集中！</strong>採用情報はこちら</div>
  </div>
</section>

<div class="map" role="img" aria-label="クリニック周辺の地図"></div>

<footer class="site-footer">
  <div class="footer-top">
    <div class="logo" style="position:static"><span class="logo-mark"></span><span class="logo-name">つばきゆめクリニック</span></div>
    <p class="tel">☎ 00-0000-0000</p>
    <div class="contact-btn">お問い合わせ</div>
  </div>
  <div class="footer-body">
    <div class="footer-address">
      <p>〒000-0000 東京都つばき区ゆめ町1-2-3 つばきビル3階</p>
      <div class="box">診療時間表</div>
    </div>
    <ul class="footer-nav">
      <li>TOP</li><li>よくある質問</li><li>うつ病</li>
      <li>当院について</li><li>お知らせ</li><li>統合失調症</li>
      <li>初めての方へ</li><li>ブログ</li><li>認知症</li>
      <li>医師の紹介</li><li>お問い合わせ</li><li>不安障害</li>
      <li>診療の流れ</li><li>採用情報</li><li>睡眠障害</li>
    </ul>
  </div>
  <p class="copyright">© Tsubaki Yume Clinic</p>
</footer>

</body>
</html>
```